Personal Injury Lawyer Billboard

I would like a design created featuring the image of the lawyer centered in the middle of the design.
To the left of the lawyer's image it should read "INJURED?"
To the right of the lawyer's image, it should read "CALL BRUNO!"
Under Call Bruno, include the phone number 318-555-0187.
At the bottom of the design include the lawyers information "Bruno Pemberly Accident & Injury Lawyers"
PLEASE REMOVED THE BACKGROUND IMAGERY OF THE PHOTO SUBMITTED. Also, the colors for this design should match the colors shown in the logo (navy, white and relective soft gold). Please use those color combinations in ways that best stand out.

```html
<!DOCTYPE html>
<html lang="en">
<head>
<meta charset="UTF-8">
<title>Injured? Call Bruno! Billboard</title>
<link rel="stylesheet" href="https://fonts.googleapis.com/css2?family=Anton&family=Bebas+Neue&family=Cinzel:wght@700&display=swap">
<style>
  :root {
    --navy: #0f1c45;
    --navy-deep: #0b1638;
    --gold: #e1a42c;
    --gold-light: #e8b444;
    --gold-shadow: #9c6a17;
    --white: #ffffff;
    --page: #d9d9d9;
  }
  * { margin: 0; padding: 0; box-sizing: border-box; }
  html, body {
    width: 1091px;
    height: 1200px;
    overflow: hidden;
    background: var(--page);
  }
  .canvas {
    position: relative;
    width: 1091px;
    height: 1200px;
  }
  .billboard {
    position: absolute;
    left: 30px;
    top: 430px;
    width: 1031px;
    height: 341px;
    background: var(--white);
    box-shadow: 0 10px 24px rgba(0,0,0,0.35);
    overflow: hidden;
  }
  .billboard__panels {
    position: absolute;
    left: 0;
    top: 0;
    width: 1031px;
    height: 271px;
  }
  .lawyer-photo {
    position: absolute;
    left: 407px;
    top: 17px;
    width: 237px;
    height: 254px;
    background: linear-gradient(180deg, #c99a7a 0%, #b8876a 30%, #1e2a5c 45%, #18224e 100%);
    border-radius: 110px 110px 0 0;
  }
  .headline {
    position: absolute;
    left: 27px;
    top: 24px;
    font-family: "Anton", sans-serif;
    font-size: 118px;
    line-height: 1;
    color: var(--navy);
    -webkit-text-stroke: 3px var(--white);
    paint-order: stroke fill;
    text-shadow: -8px 8px 0 var(--gold-shadow);
    letter-spacing: -1px;
  }
  .firm-name {
    position: absolute;
    left: 40px;
    top: 180px;
    width: 262px;
    font-family: "Cinzel", serif;
    font-weight: 700;
    font-size: 17px;
    line-height: 1.35;
    color: var(--navy);
    letter-spacing: 0.5px;
  }
  .cta {
    position: absolute;
    right: 36px;
    top: 32px;
    font-family: "Bebas Neue", sans-serif;
    font-size: 98px;
    line-height: 1;
    color: var(--white);
    letter-spacing: 1px;
  }
  .cta__name { color: var(--gold); }
  .phone {
    position: absolute;
    right: 36px;
    top: 129px;
    font-family: "Bebas Neue", sans-serif;
    font-size: 84px;
    line-height: 1;
    color: var(--white);
    letter-spacing: 1px;
  }
  .website {
    position: absolute;
    right: 36px;
    top: 229px;
    font-family: "Bebas Neue", sans-serif;
    font-size: 29px;
    line-height: 1;
    color: var(--white);
    letter-spacing: 2px;
  }
  .footer-band {
    position: absolute;
    left: 0;
    top: 271px;
    width: 1031px;
    height: 70px;
    display: flex;
    align-items: center;
    justify-content: center;
    font-family: "Cinzel", serif;
    font-weight: 700;
    font-size: 30px;
    letter-spacing: 2.5px;
    color: var(--navy);
    text-transform: uppercase;
  }
</style>
</head>
<body>
<main class="canvas">
  <section class="billboard">
    <svg class="billboard__panels" viewBox="0 0 1031 271" width="1031" height="271" aria-hidden="true">
      <defs>
        <linearGradient id="goldSheen" x1="0" y1="0" x2="1" y2="1">
          <stop offset="0" stop-color="#e6b445"/>
          <stop offset="1" stop-color="#e2a533"/>
        </linearGradient>
      </defs>
      <rect x="0" y="0" width="1031" height="271" fill="var(--gold)"/>
      <polygon points="226,0 490,0 610,271 360,271" fill="url(#goldSheen)"/>
      <polygon points="490,0 1031,0 1031,271 610,271" fill="var(--navy)"/>
      <rect x="573" y="130" width="458" height="82" fill="var(--gold)"/>
    </svg>

    <div class="lawyer-photo" role="img" aria-label="Portrait photo of the lawyer in a navy suit and green tie, smiling with a raised fist"></div>

    <h1 class="headline">INJURED?</h1>

    <p class="firm-name">BRUNO PEMBERLY<br>ACCIDENT &amp; INJURY LAWYERS</p>

    <p class="cta">CALL <span class="cta__name">BRUNO!</span></p>
    <p class="phone">318-555-0187</p>
    <p class="website">WWW.BRUNOPEMBERLY.COM</p>

    <p class="footer-band">Bruno Pemberly Accident &amp; Injury Lawyers</p>
  </section>
</main>
</body>
</html>
```